Building company buisness cards

We are looking for a sharp modern new look for our business cards.
We are a New Zealand based company that specialises in house and land packages.
We have attached a photo of the current logo and would like to see if it can be improved somehow if needed.
We are open to any colours but we have chosen green at this stage.
Feel free to change the font and make the logo smarter looking.
Play with the colours and see what looks best.

We want a card that looks so good know one will want to throw it away!

Target Market(s)

Home buyers

Industry/Entity Type

Building

Contact Information for Business Card

Dorian Keswick
0217392604
dkeswick@tidewellhomecraft.co.nz
tidewellhomecraft.co.nz

Font styles to use
Serif
Sans Serif

Colors

Designer to choose colors to be used in the design.

Requirements
Must have
• Logo and company name on one side, details on the other side
Nice to have
• Color codes for the original green are HEX #4a8028, RGB(74,128,40), CMYK(42,0,69,50)
• Round corners, Raised and/or spot UV

```html
<!DOCTYPE html>
<html lang="en">
<head>
<meta charset="utf-8">
<title>Tidewell Homecraft – Business Cards</title>
<link href="https://fonts.googleapis.com/css2?family=Oswald:wght@600&family=Roboto:wght@400&display=swap" rel="stylesheet">
<style>
  :root {
    --backdrop: #e9e6e1;
    --card: #ffffff;
    --brand-green: #4a8028;
    --ink: #1d1d1d;
    --rule: #6d6d6d;
  }
  * { box-sizing: border-box; margin: 0; padding: 0; }
  html, body {
    width: 1200px; height: 862px; overflow: hidden;
    background: var(--backdrop);
  }
  .sheet {
    position: relative; width: 1200px; height: 862px;
    display: flex; flex-direction: column; align-items: center; justify-content: center; gap: 40px;
  }
  .card {
    position: relative; width: 620px; height: 354px;
    background: var(--card);
    box-shadow: 0 2px 6px rgba(0,0,0,0.12);
  }

  /* Front: company name */
  .card--front {
    display: flex; align-items: center; justify-content: center; gap: 14px;
  }
  .brand-mark {
    width: 14px; height: 14px; background: var(--brand-green); flex: none;
  }
  .brand-name {
    font-family: "Roboto", sans-serif; font-weight: 400;
    font-size: 32px; letter-spacing: 1px;
    color: var(--brand-green);
    line-height: 1;
  }

  /* Back: contact details */
  .card--back {
    display: flex; align-items: center;
    padding-left: 150px;
  }
  .identity {
    display: flex; flex-direction: column; align-items: flex-end;
    font-family: "Oswald", sans-serif; font-weight: 600;
    color: var(--brand-green); text-transform: uppercase;
    line-height: 0.9;
  }
  .identity .given { font-size: 22px; letter-spacing: 1px; }
  .identity .family { font-size: 46px; letter-spacing: 1px; }
  .divider {
    width: 1px; height: 66px; background: var(--rule);
    margin: 0 16px 0 18px;
  }
  .contacts { list-style: none; font-family: "Roboto", sans-serif; font-size: 13.5px; color: var(--ink); }
  .contacts li { display: flex; align-items: center; gap: 9px; line-height: 20px; white-space: nowrap; }
  .contacts svg { width: 11px; height: 11px; fill: var(--brand-green); flex: none; }
</style>
</head>
<body>
<main class="sheet">
  <section class="card card--front" aria-label="Card front">
    <span class="brand-mark" aria-hidden="true"></span>
    <h1 class="brand-name">Tidewell Homecraft</h1>
  </section>

  <section class="card card--back" aria-label="Card back">
    <div class="identity">
      <span class="given">Dorian</span>
      <span class="family">Keswick</span>
    </div>
    <div class="divider"></div>
    <ul class="contacts">
      <li>
        <svg viewBox="0 0 24 24" aria-hidden="true"><path d="M6.6 10.8a15.2 15.2 0 0 0 6.6 6.6l2.2-2.2a1 1 0 0 1 1-.25 11.4 11.4 0 0 0 3.6.57 1 1 0 0 1 1 1V20a1 1 0 0 1-1 1A17 17 0 0 1 3 4a1 1 0 0 1 1-1h3.5a1 1 0 0 1 1 1c0 1.25.2 2.45.57 3.57a1 1 0 0 1-.25 1z"/></svg>
        <span>0217392604</span>
      </li>
      <li>
        <svg viewBox="0 0 24 24" aria-hidden="true"><path d="M2 5h20v2l-10 7L2 7z M2 9.5l10 7 10-7V19H2z"/></svg>
        <span>dkeswick@tidewellhomecraft.co.nz</span>
      </li>
      <li>
        <svg viewBox="0 0 24 24" aria-hidden="true"><path d="M12 2a10 10 0 1 0 0 20 10 10 0 0 0 0-20zm6.9 6h-3a15.6 15.6 0 0 0-1.4-3.6A8 8 0 0 1 18.9 8zM12 4a14 14 0 0 1 1.9 4h-3.8A14 14 0 0 1 12 4zM4.3 14a8 8 0 0 1 0-4h3.4a16.5 16.5 0 0 0 0 4zm.8 2h3a15.6 15.6 0 0 0 1.4 3.6A8 8 0 0 1 5.1 16zm3-8h-3a8 8 0 0 1 4.4-3.6A15.6 15.6 0 0 0 8.1 8zM12 20a14 14 0 0 1-1.9-4h3.8A14 14 0 0 1 12 20zm2.3-6H9.7a14.7 14.7 0 0 1 0-4h4.6a14.7 14.7 0 0 1 0 4zm.3 5.6a15.6 15.6 0 0 0 1.4-3.6h3a8 8 0 0 1-4.4 3.6zM16.3 14a16.5 16.5 0 0 0 0-4h3.4a8 8 0 0 1 0 4z"/></svg>
        <span>www.tidewellhomecraft.co.nz</span>
      </li>
    </ul>
  </section>
</main>
</body>
</html>
```